Postcard Design

Our company

"Flerndo" is the premier, next-generation cleaning company.

We offer On-Demand hourly cleaning services at the touch of a button, we’re available 24/7/and our bonded, insured cleaners are the best in the business. (works like KAVO) www.flerndo-example.com

Headquarters in Chicago, IL. Flerndo is expanding to 13 cities nationwide within 12 months

Industry/Entity Type

Business

Requirements
Must have
• One Free home Cleaning

```html
<!DOCTYPE html>
<html lang="en">
<head>
<meta charset="utf-8">
<title>Flerndo Postcard</title>
<link href="https://fonts.googleapis.com/css2?family=Roboto+Condensed:ital,wght@0,400;0,700;1,400&family=Arimo:wght@400;700&display=swap" rel="stylesheet">
<style>
  :root {
    --green: #62a330;
    --green-light: #a8cf5c;
    --green-pale: #d7ebb4;
    --purple: #6b2a88;
    --magenta: #b3238c;
    --beige: #ede8dc;
    --blue: #1f78c1;
    --ink: #222;
    --stage: #f2f2f2;
    --white: #fff;
  }
  * { box-sizing: border-box; margin: 0; padding: 0; }
  html, body { width: 976px; height: 1200px; overflow: hidden; background: var(--stage); }
  body { position: relative; font-family: "Arimo", Arial, sans-serif; color: var(--ink); }

  .card { position: absolute; background: var(--white); overflow: hidden; box-shadow: 0 2px 8px rgba(0,0,0,.14); }
  .card--front { left: 40px; top: 24px; width: 708px; height: 547px; }
  .card--back { left: 198px; top: 595px; width: 744px; height: 588px; }
  .abs { position: absolute; }

  /* front */
  .front-scene { left: 0; top: 0; width: 708px; height: 547px; background: linear-gradient(90deg, #e9ece8 0%, #f7f8f6 45%, #eef0ee 100%); }
  .front-person { left: 82px; top: 10px; width: 295px; height: 372px; background: radial-gradient(ellipse at 50% 32%, #e8cbb5 0%, #c9b39b 28%, #8fbb57 55%, rgba(233,236,232,0) 80%); }
  .front-ground { left: 0; top: 360px; }

  .brand { left: 344px; top: 52px; display: flex; align-items: center; gap: 12px; }
  .brand-dot { width: 64px; height: 64px; border-radius: 50%; border: 4px solid var(--green-light); }
  .brand-name { font-family: "Roboto Condensed", sans-serif; font-weight: 400; font-size: 46px; letter-spacing: 4px; color: var(--green); line-height: 1; }
  .tagline { left: 436px; top: 104px; font-family: "Roboto Condensed", sans-serif; font-style: italic; font-size: 17px; letter-spacing: 1px; color: var(--green-light); }

  .quote { right: 41px; top: 150px; text-align: right; font-family: "Roboto Condensed", sans-serif; font-size: 16px; color: var(--green); line-height: 1.3; }
  .quote-by { display: block; margin-top: 8px; margin-right: 8px; font-style: italic; font-size: 16px; }

  .offer-art { left: 430px; top: 240px; width: 62px; height: 110px; border-radius: 8px; background: linear-gradient(160deg, #d9c3df, var(--magenta) 70%); }
  .offer { left: 475px; top: 252px; width: 197px; height: 62px; border-radius: 8px; background: var(--green-light); color: var(--white); text-align: center; font-family: "Roboto Condensed", sans-serif; padding-top: 4px; }
  .offer-big { font-weight: 700; font-size: 30px; line-height: 1; }
  .offer-small { font-size: 19px; line-height: 1.15; }

  .badge-247 { left: 35px; top: 311px; }
  .badges { left: 313px; top: 372px; }

  .contact { display: flex; align-items: center; gap: 8px; font-size: 14px; font-weight: 700; line-height: 1; }
  .front-mail { left: 30px; top: 497px; }
  .front-phone { left: 258px; top: 495px; }
  .front-web { right: 37px; top: 496px; font-size: 18px; font-weight: 700; color: var(--green); }

  /* back */
  .back-top { left: 0; top: 0; }
  .headline { left: 30px; top: 74px; font-weight: 700; font-size: 20px; color: var(--green); }
  .stat { top: 100px; width: 110px; text-align: center; }
  .stat--hours { left: 15px; }
  .stat--days { left: 115px; }
  .stat--sure { left: 219px; }
  .stat-num { font-weight: 700; font-size: 38px; color: var(--green); line-height: 1; }
  .stat-label { font-size: 12px; margin-top: 5px; }
  .back-mark { left: 384px; top: 34px; width: 120px; height: 120px; border-radius: 50%; background: var(--white); border: 6px solid var(--green-light); }

  .back-lead { left: 42px; top: 214px; font-weight: 700; font-size: 14px; color: var(--green); }
  .back-quote { right: 406px; top: 232px; text-align: right; font-weight: 700; font-size: 14px; color: var(--green); line-height: 1.2; }
  .back-quote-by { right: 411px; top: 268px; font-size: 14px; color: var(--green-light); }
  .back-photo { left: 40px; top: 290px; width: 320px; height: 92px; background: linear-gradient(90deg, #dfe6d8 0%, #f4f4f2 30%, #8bbd4d 62%, #eeeeea 100%); }
  .slogan { left: 94px; top: 418px; font-family: "Roboto Condensed", sans-serif; font-size: 17px; color: var(--green); }
  .slogan-lead { color: var(--blue); }
  .back-phone { left: 232px; top: 442px; font-size: 13px; }
  .back-mail { left: 60px; top: 468px; font-size: 13px; }
  .back-web { left: 100px; top: 490px; font-size: 18px; font-weight: 700; color: var(--green); }
</style>
</head>
<body>

<section class="card card--front">
  <div class="abs front-scene" role="img" aria-label="Bright living room backdrop"></div>
  <div class="abs front-person" role="img" aria-label="Smiling cleaner in a green apron holding a caddy of cleaning supplies"></div>

  <svg class="abs front-ground" width="708" height="187" viewBox="0 0 708 187" aria-hidden="true">
    <path d="M0 18 C 200 95, 500 95, 708 0 L708 14 C 500 108, 200 108, 0 32 Z" fill="var(--green-pale)"/>
    <path d="M0 32 C 200 108, 500 108, 708 14 L708 30 C 500 122, 200 122, 0 46 Z" fill="var(--green-light)"/>
    <path d="M0 46 C 200 122, 500 122, 708 30 L708 187 L0 187 Z" fill="var(--white)"/>
  </svg>

  <div class="abs brand"><span class="brand-dot"></span><span class="brand-name">FLERNDO</span></div>
  <div class="abs tagline">Cleaning You Can Trust</div>

  <p class="abs quote">"Wow! Where did you folks come from<br>I called, you came and cleaned."<span class="quote-by">W. H. - Chicago</span></p>

  <div class="abs offer-art" role="img" aria-label="House and squeegee illustration"></div>
  <div class="abs offer"><div class="offer-big">ONE FREE</div><div class="offer-small">HOME CLEANING</div></div>

  <svg class="abs badge-247" width="160" height="160" viewBox="0 0 160 160" aria-label="24/7 on-demand hourly cleaning services">
    <circle cx="80" cy="80" r="74" fill="var(--white)" stroke="var(--green)" stroke-width="4"/>
    <circle cx="80" cy="80" r="66" fill="none" stroke="var(--green-light)" stroke-width="1.5"/>
    <path d="M84 22 A 56 56 0 0 1 126 104" fill="none" stroke="var(--purple)" stroke-width="7" stroke-linecap="round"/>
    <text x="72" y="86" text-anchor="middle" font-family="Roboto Condensed, sans-serif" font-weight="700" font-style="italic" font-size="42" fill="var(--green)">24<tspan fill="var(--purple)">/7</tspan></text>
    <text x="80" y="112" text-anchor="middle" font-family="Arimo, sans-serif" font-weight="700" font-size="8" fill="var(--green)">ON-DEMAND HOURLY</text>
    <text x="80" y="123" text-anchor="middle" font-family="Arimo, sans-serif" font-weight="700" font-size="8" fill="var(--green)">CLEANING SERVICES</text>
  </svg>

  <svg class="abs badges" width="370" height="120" viewBox="0 0 370 120" aria-label="Service promises">
    <defs>
      <path id="arc-time" d="M26.2 79.5 A 39 39 0 1 1 93.8 79.5"/>
      <path id="arc-bond" d="M150.2 79.5 A 39 39 0 1 1 217.8 79.5"/>
      <path id="arc-best" d="M272.2 79.5 A 39 39 0 1 1 339.8 79.5"/>
    </defs>
    <g font-family="Roboto Condensed, sans-serif" font-weight="700" font-size="11.5" fill="var(--white)">
      <circle cx="60" cy="60" r="52" fill="var(--green)"/>
      <circle cx="60" cy="60" r="33" fill="var(--white)"/>
      <text><textPath href="#arc-time" startOffset="50%" text-anchor="middle">We Hate Wasting Time</textPath></text>
      <circle cx="60" cy="60" r="10" fill="none" stroke="var(--green)" stroke-width="2"/>
      <path d="M60 54 V60 H65" stroke="var(--green)" stroke-width="2" fill="none"/>

      <circle cx="184" cy="60" r="52" fill="var(--green)"/>
      <circle cx="184" cy="60" r="33" fill="var(--white)"/>
      <text><textPath href="#arc-bond" startOffset="50%" text-anchor="middle">Guaranteed and Bonded</textPath></text>
      <path d="M174 61 L181 68 L195 52" stroke="var(--green)" stroke-width="3" fill="none"/>

      <circle cx="306" cy="60" r="52" fill="var(--green)"/>
      <circle cx="306" cy="60" r="33" fill="var(--white)"/>
      <text><textPath href="#arc-best" startOffset="50%" text-anchor="middle">Best Cleaners in TOWN</textPath></text>
      <path d="M298 50 H314 V56 A8 8 0 0 1 298 56 Z M306 64 V70 M300 72 H312" stroke="var(--green)" stroke-width="2" fill="none"/>
    </g>
  </svg>

  <div class="abs contact front-mail">
    <svg width="26" height="18" viewBox="0 0 26 18" aria-hidden="true"><rect x="1" y="1" width="24" height="16" fill="none" stroke="var(--green)" stroke-width="2"/><path d="M1 1 L13 10 L25 1" fill="none" stroke="var(--green)" stroke-width="2"/></svg>
    <span>info@flerndo-example.com</span>
  </div>
  <div class="abs contact front-phone">
    <svg width="26" height="22" viewBox="0 0 26 22" aria-hidden="true"><path d="M13 2 C6 2 2 6 2 10 C2 13 4 15 7 16 L5 21 L12 17 C19 17 24 14 24 10 C24 6 20 2 13 2 Z" fill="none" stroke="var(--green)" stroke-width="2"/></svg>
    <span>312-555-0147</span>
  </div>
  <div class="abs front-web">www.flerndo-example.com</div>
</section>

<section class="card card--back">
  <svg class="abs back-top" width="744" height="230" viewBox="0 0 744 230" aria-hidden="true">
    <path d="M0 0 H600 C 500 40, 430 130, 300 155 C 190 172, 80 172, 0 170 Z" fill="var(--beige)"/>
    <path d="M0 170 C 80 172, 190 172, 300 155 C 430 130, 500 40, 600 0 L628 0 C 520 60, 450 160, 300 188 C 190 204, 80 204, 0 200 Z" fill="var(--green-light)"/>
    <path d="M0 200 C 80 204, 190 204, 300 188 C 450 160, 520 60, 628 0 L642 0 C 532 70, 462 174, 300 199 C 190 214, 80 214, 0 210 Z" fill="var(--green-pale)"/>
  </svg>
  <h2 class="abs headline">We tame the toughest messes!</h2>
  <div class="abs stat stat--hours"><div class="stat-num">24</div><div class="stat-label">Hours a day</div></div>
  <div class="abs stat stat--days"><div class="stat-num">7</div><div class="stat-label">Days a Week</div></div>
  <div class="abs stat stat--sure"><div class="stat-num">100</div><div class="stat-label">% Guaranteed</div></div>
  <div class="abs back-mark" aria-hidden="true"></div>

  <p class="abs back-lead">Flerndo makes everything simple and clean</p>
  <p class="abs back-quote">"My bathrooms have not looked this good<br>in 16 years!"</p>
  <p class="abs back-quote-by">C. R. - Chicago</p>
  <div class="abs back-photo" role="img" aria-label="Cleaner in a green top wiping a window with a cloth"></div>

  <p class="abs slogan"><span class="slogan-lead">WE LOVE TO CLEAN,</span> AND IT SHOWS!</p>
  <div class="abs contact back-phone">
    <svg width="26" height="22" viewBox="0 0 26 22" aria-hidden="true"><path d="M13 2 C6 2 2 6 2 10 C2 13 4 15 7 16 L5 21 L12 17 C19 17 24 14 24 10 C24 6 20 2 13 2 Z" fill="none" stroke="var(--green)" stroke-width="2"/></svg>
    <span>312-555-0147</span>
  </div>
  <div class="abs contact back-mail">
    <svg width="26" height="18" viewBox="0 0 26 18" aria-hidden="true"><rect x="1" y="1" width="24" height="16" fill="none" stroke="var(--green)" stroke-width="2"/><path d="M1 1 L13 10 L25 1" fill="none" stroke="var(--green)" stroke-width="2"/></svg>
    <span>info@flerndo-example.com</span>
  </div>
  <div class="abs back-web">www.flerndo-example.com</div>
</section>

</body>
</html>
```